Wordpress Design Project

Hello, my name is Dermot Vasey and I am a Professor at a university in Hong Kong. I am looking for a clean and professional website to introduce myself with my bio, resume, and contact info. Looking for a creative & professional personal website, because all the information is very textual and I am looking forward to see how you can make it look good.
Updates
Project Deadline Extended
Reason: Can't find a satisfying design so far. Looking forward to see better ones.
I have added a zip file call "Good Examples" please look at the screenshot I attach. These are the quality that I am looking forward to see in your work.
Project Deadline Extended
Reason: It looks like we need more time
Project Deadline Extended
Reason: Need more time, waiting for designs
Target Market(s)
Potential Business Clients & Partners
Industry/Entity Type
University
Requirements
Must have
- The Design:
Please include photos of the schools I went to, e.g. Pellham College in Michigan, read my resume for more. You can also download the logos of the organization or institute and include them in my website to make the website more professional, just make sure the logo you found on google is correct.
The Development:
The final deliverable must be a fully coded, functional website. Site must be tested and good to go in IE 7+, Firefox 9+, Chrome and both Apple and Android Mobile platforms. Blog must be one that church can easily upload content to as an integrated part of the site (no Jotlane.com, etc plugins please).
Final handover must include full rights to the designs, stock art, coding, etc (so, no "one use templates" please).
Final handover will include loading and testing on to our hosting server.
The designer must be willing to support the site for 30 days after launch as part of the site payment.
Nice to have
- I have attached some scanned photos of myself. They are really blurry and low quality, can you do some touch ups in photoshop? Because I would still love to have the photos appear somewhere in the website (e.g. inside a banner).
You can also find my photos on google by searching my name "Dermot Vasey", just make sure you find the right one.
Should not have
- Anything that looks cheap and amateurish, no flash. Anything that looks like a cookie cutter website.

```html
<!DOCTYPE html>
<html lang="en">
<head>
<meta charset="utf-8">
<title>Prof. Dermot Vasey MH</title>
<link href="https://fonts.googleapis.com/css2?family=Tinos:wght@400;700&family=PT+Sans:wght@400;700&family=Oswald:wght@500&display=swap" rel="stylesheet">
<style>
:root{
  --navy:#1a3c86;
  --navy-dark:#0e2c5e;
  --ink-blue:#1f3f95;
  --body-grey:#5e5e5e;
  --line:#dcdcdc;
  --band:#f3f2ee;
  --white:#ffffff;
}
*{margin:0;padding:0;box-sizing:border-box}
html,body{width:1011px;height:1200px;overflow:hidden;background:var(--white)}
body{position:relative;font-family:"PT Sans",sans-serif;color:var(--body-grey)}
.abs{position:absolute}

/* header */
.site-header{left:0;top:0;width:1011px;height:91px;border-bottom:1px solid var(--line);background:var(--white)}
.site-title{left:43px;top:32px;font-family:"Tinos",serif;font-size:28px;color:var(--navy);font-weight:400}
.site-degrees{left:234px;top:65px;font-size:11px;color:var(--navy)}
.main-nav{left:442px;top:27px;width:518px;height:50px;background:linear-gradient(#2757a8,#173f88);border-radius:4px;display:flex;align-items:center;justify-content:space-around;padding:0 8px}
.main-nav a{font-family:"Tinos",serif;color:var(--white);text-decoration:none;font-size:14px;letter-spacing:.3px}
.main-nav .sep{width:1px;height:18px;background:rgba(255,255,255,.35)}

/* hero */
.hero{left:0;top:92px;width:1011px;height:412px;background:linear-gradient(180deg,#ffffff 0%,#f1f1f1 55%,#e4e4e2 100%);border-bottom:1px solid var(--line)}
.hero-backdrop{left:0;top:92px;width:1011px;height:412px;background:radial-gradient(ellipse at 28% 60%,rgba(190,190,188,.45),rgba(255,255,255,0) 60%)}
.hero-text{left:49px;top:172px;width:367px;font-size:12.2px;line-height:21.7px;color:var(--ink-blue);text-align:justify}
.learn-more{left:49px;top:309px;width:117px;height:32px;background:linear-gradient(#2a58a8,#163a80);border-radius:4px;color:var(--white);font-family:"Oswald",sans-serif;font-size:13.5px;display:flex;align-items:center;justify-content:center}
.slider-dots{left:52px;top:365px;display:flex;gap:4px}
.slider-dots span{width:8px;height:8px;border-radius:50%;background:#9aa6c4}
.slider-dots span:first-child{background:var(--navy)}
.hero-frame{left:471px;top:126px;width:488px;height:325px;background:var(--white);box-shadow:0 1px 4px rgba(0,0,0,.2)}
.hero-photo{left:480px;top:135px;width:470px;height:308px;background:linear-gradient(180deg,#b9d39a 0%,#dfe8d0 20%,#e8e8ec 40%,#c79a4e 75%,#8a6430 100%)}

/* features */
.features{left:0;top:504px;width:1011px;height:387px;background:linear-gradient(180deg,var(--band) 0%,var(--band) 70%,#e6e3dc 100%)}
.feature h2{font-family:"Tinos",serif;font-weight:400;font-size:20.5px;color:var(--navy);white-space:nowrap}
.feature .frame{position:absolute;top:27px;left:0;width:265px;height:115px;background:var(--white);box-shadow:0 0 3px rgba(0,0,0,.25)}
.feature .photo{position:absolute;top:5px;left:5px;width:255px;height:105px}
.feature p{position:absolute;top:150px;left:0;width:260px;font-size:11.4px;line-height:19px;color:var(--body-grey)}
.feature .read-more{position:absolute;top:255px;left:0;font-family:"Tinos",serif;font-weight:700;font-size:14.5px;color:var(--navy)}
.contact-tab{left:772px;top:856px;width:153px;height:35px;background:linear-gradient(#2a58a8,#173c82);border-radius:22px 22px 0 0;color:var(--white);font-family:"Tinos",serif;font-size:15.5px;display:flex;align-items:center;justify-content:center}

/* contact */
.contact-info{left:58px;top:929px}
.section-label{font-family:"Tinos",serif;font-weight:700;font-size:15.5px;color:var(--navy);letter-spacing:.3px;display:flex;align-items:center;gap:8px}
.contact-info ul{list-style:none;margin-top:12px}
.contact-info li{font-size:11.4px;line-height:22.6px;color:#333}
.contact-info li.role{color:#111}
.contact-info a{color:#333}
.divider{left:302px;top:922px;width:1px;height:170px;background:var(--line)}
.message-form{left:331px;top:931px}
.field-label{position:absolute;font-size:12px;color:#333;white-space:nowrap}
.field{position:absolute;border:1px solid #cfcfcf;border-radius:4px;background:var(--white)}
.send-btn{left:807px;top:1054px;width:74px;height:28px;background:linear-gradient(#2a58a8,#163a80);border-radius:3px;color:var(--white);font-family:"Tinos",serif;font-size:14px;display:flex;align-items:center;justify-content:center}

/* footer */
.site-footer{left:0;top:1151px;width:1011px;height:49px;background:var(--navy-dark);color:var(--white);font-size:10.5px}
.copyright{left:60px;top:14px}
.footer-nav{right:44px;top:14px;display:flex;gap:9px}
.footer-nav span.bar{opacity:.7}
</style>
</head>
<body>

<header class="site-header abs">
  <div class="site-title abs">Prof. Dermot Vasey MH</div>
  <div class="site-degrees abs">BA, MA, PhD</div>
  <nav class="main-nav abs">
    <a>HOME</a><span class="sep"></span>
    <a>BIO</a><span class="sep"></span>
    <a>CONTRIBUTIONS</a><span class="sep"></span>
    <a>ACHIEVEMENTS</a><span class="sep"></span>
    <a>CONTACT</a>
  </nav>
</header>

<section class="hero abs"></section>
<div class="hero-backdrop abs" role="img" aria-label="Faint sketch of a university campus building"></div>
<p class="hero-text abs">Dermot actively promotes the value of sound HR practices and work-life balance in Hong Kong. He has served on the board of the Fair Access Council and is currently a board member of different NGOs and schools in Hong Kong. He has been invited to be a panel judge/adjudicator for various competitions and events promoting good human resource management and equal</p>
<div class="learn-more abs">LEARN MORE</div>
<div class="slider-dots abs"><span></span><span></span><span></span><span></span></div>
<div class="hero-frame abs"></div>
<div class="hero-photo abs" role="img" aria-label="Photo of Prof. Vasey speaking on a forum panel about human capital, seated with three fellow panellists"></div>

<section class="features abs" role="img" aria-label="Faint campus building illustration along the lower edge"></section>

<article class="feature abs" style="left:69px;top:549px">
  <h2>Education &amp; Qualifications</h2>
  <div class="frame"><div class="photo" role="img" aria-label="Photo of Prof. Vasey receiving an award at a school ceremony" style="background:linear-gradient(120deg,#c8231c,#e04a2a 60%,#f1d9c4)"></div></div>
  <p>Dermot received his secondary school education in HK and obtained his BA, MA, and PhD in the US. Specializing in Strategy Human Resource Management and Labor Relations, he is a certified Senior Professional in Human Resources</p>
  <div class="read-more">Read more..</div>
</article>

<article class="feature abs" style="left:369px;top:549px">
  <h2>Career &amp; Services</h2>
  <div class="frame"><div class="photo" role="img" aria-label="Photo of Prof. Vasey with a colleague at a career event" style="background:linear-gradient(120deg,#d7a8d8,#f2d9ef 50%,#8a6aa8)"></div></div>
  <p>Dermot is now a professor in the Department of Management at Harbourview University. Before he began his career in teaching and management consulting, he held managerial positions in the health, manufacturing and banking</p>
  <div class="read-more">Read more..</div>
</article>

<article class="feature abs" style="left:669px;top:549px">
  <h2>Awards and Honors</h2>
  <div class="frame"><div class="photo" role="img" aria-label="Photo of Prof. Vasey with a guest in a garden after an honours ceremony" style="background:linear-gradient(120deg,#2f6a2a,#5d9a40 55%,#c9b89a)"></div></div>
  <p>He was awarded the Outstanding Human Resource Educational Elite in Greater China Award in 2004 and Outstanding Contribution to HR Award in 2010. In 2012, Prof. Vasey was awarded the Medal of Honour by the Hong Kong</p>
  <div class="read-more">Read more..</div>
</article>

<div class="contact-tab abs">Contact Me</div>

<section class="contact-info abs">
  <div class="section-label">CONTACT INFO
    <svg width="23" height="15" viewBox="0 0 23 15"><rect width="23" height="15" fill="#1a3c86"/><path d="M0 0 L11.5 9 L23 0" fill="none" stroke="#fff" stroke-width="1.6"/></svg>
  </div>
  <ul>
    <li class="role">Professor of Human Resource Management</li>
    <li>Department of Management</li>
    <li>School of Business</li>
    <li>Harbourview University</li>
    <li>Email:&nbsp; <a>dvasey@harbourview.edu</a></li>
  </ul>
</section>

<div class="divider abs"></div>

<section class="message-form abs">
  <div class="section-label">MESSAGE DERMOT</div>
</section>
<span class="field-label abs" style="left:332px;top:970px">First Name</span>
<span class="field abs" style="left:397px;top:963px;width:203px;height:27px"></span>
<span class="field-label abs" style="left:332px;top:1008px">Last Name</span>
<span class="field abs" style="left:397px;top:1003px;width:203px;height:27px"></span>
<span class="field-label abs" style="left:332px;top:1049px">Subject</span>
<span class="field abs" style="left:397px;top:1043px;width:203px;height:27px"></span>
<span class="field-label abs" style="left:629px;top:968px">Message</span>
<span class="field abs" style="left:680px;top:960px;width:202px;height:88px"></span>
<div class="send-btn abs">SEND</div>

<footer class="site-footer abs">
  <div class="copyright abs">Copyright (copyright logo) 2013 DermotVasey.com &amp; Prof. Dermot K Vasey All Rights Reserved</div>
  <div class="footer-nav abs"><span>Home</span><span class="bar">|</span><span>Terms of Use</span><span class="bar">|</span><span>Sitemap</span><span class="bar">|</span><span>Contact</span></div>
</footer>

</body>
</html>
```